vSTRIDE Membership Flyer

vSTRIDE is a shoe store selling brand name sneakers like Zelo Morvan Kesto Tavrin and etc. We need a flyer to promote our membership program. On this flyer we need to emphasize that people who sign up can get 20% off their entire first purchase(certain items are excluded), which is limited time offer.
The flyer is 5.5"X4.25", two sided.
On the back side, there need to be a section where customer can fill up their name, phone number and email to join the membership.
our website is www.vstridestore.example
Member benefits can also be found on the website and should be on the flyer.

Industry/Entity Type

Shoe Store

```html
<!DOCTYPE html>
<html lang="en">
<head>
<meta charset="utf-8">
<title>vSTRIDE Membership Flyer</title>
<link rel="stylesheet" href="https://fonts.googleapis.com/css2?family=Arimo:ital,wght@0,400;0,700;1,400;1,700&display=swap">
<style>
  :root {
    --orange: #ef5124;
    --peach: #f7b89c;
    --green: #1f9a45;
    --white: #ffffff;
    --ink: #1c1c1c;
    --red: #e2371f;
    --sheet: #ffffff;
    --photo-light: #f1ece6;
    --photo-mid: #c9b79a;
    --photo-blue: #5fb6cc;
  }
  * { box-sizing: border-box; margin: 0; padding: 0; }
  html, body { width: 773px; height: 1200px; overflow: hidden; background: var(--sheet); }
  body { position: relative; font-family: "Arimo", Arial, sans-serif; color: var(--ink); }

  .side-label { position: absolute; left: 40px; font-size: 15px; font-weight: 700; }
  .side-label--front { top: 10px; }
  .side-label--back { top: 604px; }

  .front { position: absolute; left: 22px; top: 33px; width: 732px; height: 558px; overflow: hidden; border: 1px solid #ddd; }
  .front__photo {
    position: absolute; inset: 0 0 41px 0;
    background: linear-gradient(120deg, var(--photo-mid) 0%, var(--photo-light) 35%, var(--photo-light) 55%, var(--photo-blue) 80%, #e8d9b0 100%);
  }
  .front__brand { position: absolute; right: 26px; top: 34px; font-size: 34px; font-weight: 700; color: var(--green); letter-spacing: 1px; }
  .offer {
    position: absolute; left: 60px; top: 40px; width: 420px; text-align: center;
    transform: rotate(-19deg); transform-origin: center;
  }
  .offer__brand { position: absolute; left: 6px; top: -8px; font-size: 18px; font-weight: 700; color: var(--green); }
  .offer__lead { font-size: 36px; color: var(--ink); margin-top: 30px; }
  .offer__big { font-size: 92px; font-weight: 700; color: var(--green); line-height: 1; }
  .offer__tail { font-size: 34px; color: var(--ink); margin-top: 4px; }
  .offer__note { font-size: 14px; font-style: italic; color: var(--red); margin-top: 6px; line-height: 1.2; }
  .front__band {
    position: absolute; left: 0; right: 0; bottom: 0; height: 41px; background: var(--orange);
    color: var(--white); font-size: 25px; text-align: center; line-height: 41px;
  }

  .back { position: absolute; left: 22px; top: 632px; width: 732px; height: 564px; display: flex; }
  .benefits { width: 377px; background: var(--orange); color: var(--white); padding: 42px 22px 0 34px; }
  .benefits__title { font-size: 25px; font-weight: 700; font-style: italic; margin-bottom: 22px; }
  .benefits__intro { font-size: 12.5px; font-weight: 700; font-style: italic; line-height: 1.35; margin-bottom: 22px; }
  .benefit { font-size: 12.5px; line-height: 1.35; margin-bottom: 22px; }
  .benefit b { font-style: italic; }
  .join { flex: 1; background: var(--peach); position: relative; padding: 0 24px 0 30px; }
  .join__brand { position: absolute; right: 30px; top: 38px; font-size: 32px; font-weight: 700; color: var(--green); letter-spacing: 1px; }
  .join__site { position: absolute; right: 30px; top: 80px; font-size: 15px; font-style: italic; }
  .join__title { position: absolute; left: 30px; top: 277px; font-size: 17px; font-weight: 700; }
  .field { position: absolute; left: 30px; font-size: 19px; font-weight: 700; white-space: nowrap; }
  .field--name { top: 335px; }
  .field--name2 { top: 375px; }
  .field--phone { top: 432px; }
  .field--email { top: 492px; }
</style>
</head>
<body>
  <div class="side-label side-label--front">Front</div>
  <section class="front">
    <div class="front__photo" role="img" aria-label="Photo of a smiling woman using a laptop, looking back over her shoulder"></div>
    <div class="front__brand">vSTRIDE</div>
    <div class="offer">
      <div class="offer__brand">vSTRIDE</div>
      <div class="offer__lead">Signup &amp; Get</div>
      <div class="offer__big">20% OFF</div>
      <div class="offer__tail">On First Purchase !</div>
      <div class="offer__note">(certain item are excluded)<br>*Limited time offer</div>
    </div>
    <div class="front__band">www.vstridestore.example</div>
  </section>

  <div class="side-label side-label--back">Back</div>
  <section class="back">
    <div class="benefits">
      <h2 class="benefits__title">Benefits :</h2>
      <p class="benefits__intro">The vSTRIDE Member Program entitles Members to the following benefits :</p>
      <p class="benefit"><b>a.&nbsp;&nbsp;&nbsp; 20% OFF your entire first purchase after you sign up (Limited Time Offer).</b> Certain items are excluded from this offer. Please see stores for details.</p>
      <p class="benefit"><b>b.&nbsp;&nbsp;&nbsp; 10% OFF every purchase while being a member.</b> Certain items are excluded from this offer. Please see stores for details.</p>
      <p class="benefit"><b>c.&nbsp;&nbsp;&nbsp; Additional 10% OFF and FREE SHIPPING</b> when an item is out of stock in store but can be shipped to you from another location.</p>
      <p class="benefit"><b>d.&nbsp;&nbsp;&nbsp; Eligible to purchase exclusive items offered to members only.</b> Purchasing of exclusive items is limited to 1 item per member per 30 days. Please see stores for details.</p>
    </div>
    <div class="join">
      <div class="join__brand">vSTRIDE</div>
      <div class="join__site">www.vstridestore.example</div>
      <div class="join__title">TO JOIN THE MEMBERSHIP</div>
      <div class="field field--name">NAME : ..........................................</div>
      <div class="field field--name2">&nbsp;.......................................................</div>
      <div class="field field--phone">PH. NUMBER : ...............................</div>
      <div class="field field--email">EMAIL : .........................................</div>
    </div>
  </section>
</body>
</html>
```